R.T. Framers Postcard Design

We need a postcard designed around the utility rebates for window installations. For customers who have Electric heated homes can receive $6 per square foot for each window and patio door and for Natural gas heated homes, they can get $75.00 per window and patio door. The $6 per square foot for electric heated customers is the better rebate averaging about $1000.00 for a house with 10 windows and a patio door. Our Company colors are maroon, black and white, we would like to have a post card designed around these colors. The postcard should be designed to share about these 2 rebates and having a window installation theme. You can use pictures off of our website...www.rtframers-example.com

Target Market(s)

Homeowners with electric heat or Natural gas heat

Industry/Entity Type

Utility

Requirements
Must have
• Blank white square on the back for me to hand write address information.

```html
<!DOCTYPE html>
<html lang="en">
<head>
<meta charset="utf-8">
<title>R.T. Framers Postcard</title>
<link href="https://fonts.googleapis.com/css2?family=Open+Sans:wght@400;700&family=Roboto:wght@900&family=Ubuntu:wght@700&display=swap" rel="stylesheet">
<style>
:root{
  --maroon:#8a0d0d;
  --red:#c1161c;
  --ink:#232021;
  --white:#ffffff;
  --grey:#d8d8d8;
  --page:#eeeeee;
}
*{margin:0;padding:0;box-sizing:border-box}
html,body{width:849px;height:1200px;overflow:hidden;background:var(--page)}
body{position:relative;font-family:"Open Sans",sans-serif;color:var(--white)}
.card{position:absolute;left:23px;width:801px;overflow:hidden}
.front{top:18px;height:570px;background:var(--ink)}
.front-bg{position:absolute;inset:0}
.brand-mark{position:absolute;left:32px;top:30px;width:190px;height:124px;display:flex;align-items:center;gap:10px}
.brand-mark .square{width:26px;height:26px;background:var(--white)}
.brand-mark span{font-family:"Roboto",sans-serif;font-weight:900;font-size:25px;color:var(--white)}
.company-name{position:absolute;left:258px;top:24px;font-family:"Roboto",sans-serif;font-weight:900;font-size:64px;letter-spacing:1px;line-height:1}
.tagline{position:absolute;left:260px;top:104px;font-family:"Roboto",sans-serif;font-weight:900;font-size:17.5px;letter-spacing:.4px}
.headline{position:absolute;left:75px;top:176px;font-family:"Ubuntu",sans-serif;font-weight:700;font-size:35px;line-height:47px;letter-spacing:1px}
.window-frame{position:absolute;left:398px;top:152px;width:362px;height:322px}
.photo{position:absolute}
.contacts{position:absolute;left:0;top:428px;width:340px}
.contact{position:relative;height:24px;margin-bottom:5px;display:flex;align-items:center;padding-left:22px;font-weight:700;font-size:16px}
.contact::before{content:"";position:absolute;inset:0;background:var(--maroon);clip-path:polygon(0 0,100% 0,97% 100%,0 100%);z-index:0}
.contact svg,.contact span{position:relative;z-index:1}
.contact svg{width:16px;height:16px;margin-right:10px}
.address-bar{position:absolute;left:352px;top:492px;width:449px;height:48px;background:var(--maroon);display:flex;align-items:flex-start;padding:4px 0 0 24px;font-weight:700;font-size:16.5px;line-height:21px}
.address-bar svg{width:14px;height:16px;margin:3px 8px 0 0;flex:none}

.back{top:614px;height:565px;background:var(--white)}
.back-panel{position:absolute;left:0;top:0;width:386px;height:471px;background:var(--ink)}
.back-corner{position:absolute;left:386px;top:0;width:243px;height:179px;background:var(--ink)}
.back-brand{position:absolute;left:33px;top:18px;display:flex;align-items:center;gap:10px}
.back-brand .square{width:26px;height:26px;background:var(--white)}
.back-brand span{font-family:"Roboto",sans-serif;font-weight:900;font-size:34px}
.rebates{position:absolute;left:33px;top:58px;width:333px}
.rebate{font-size:16.5px;line-height:22px;text-align:justify;padding:4px 0 10px;border-bottom:2px solid var(--grey);margin-bottom:6px}
.rebate:last-child{border-bottom:none}
.back-address{position:absolute;left:386px;top:38px;width:222px;text-align:right;font-size:15.5px;line-height:23px;color:var(--grey)}
.back-contacts{position:absolute;left:62px;top:340px}
.back-contact{display:flex;align-items:center;font-size:19px;line-height:28px;color:var(--grey)}
.back-contact svg{width:17px;height:17px;margin-right:13px}
</style>
</head>
<body>

<section class="card front">
  <svg class="front-bg" viewBox="0 0 801 570" aria-hidden="true">
    <rect x="0" y="0" width="250" height="570" fill="var(--red)"/>
    <path d="M250 0 C60 120 0 250 20 370 C40 470 140 540 250 570 L801 570 L801 0 Z" fill="var(--ink)"/>
  </svg>
  <div class="brand-mark"><div class="square"></div><span>R.T. Framers</span></div>
  <h1 class="company-name">R.T. FRAMERS</h1>
  <p class="tagline">YOUR LEADER IN QUALITY WINDOW INSTALLATIONS</p>
  <p class="headline">INSTALLING<br>WINDOWS<br>THE RIGHT WAY<br>EVERY TIME<br>SINCE 1985</p>

  <svg class="window-frame" viewBox="0 0 362 322">
    <rect x="0" y="0" width="362" height="22" fill="#f4f4f4"/>
    <rect x="8" y="22" width="346" height="8" fill="#e2e2e2"/>
    <rect x="14" y="30" width="334" height="262" fill="#ffffff"/>
    <rect x="8" y="292" width="346" height="10" fill="#e2e2e2"/>
    <rect x="0" y="302" width="362" height="20" fill="#f4f4f4"/>
    <rect x="34" y="56" width="298" height="202" fill="#e6e6e6"/>
    <defs>
      <linearGradient id="roomA" x1="0" y1="0" x2="0" y2="1"><stop offset="0" stop-color="#d9d4c6"/><stop offset="1" stop-color="#8b5a3c"/></linearGradient>
      <linearGradient id="roomB" x1="0" y1="0" x2="1" y2="1"><stop offset="0" stop-color="#e6ecee"/><stop offset="1" stop-color="#b9c3c2"/></linearGradient>
      <linearGradient id="roomC" x1="0" y1="0" x2="0" y2="1"><stop offset="0" stop-color="#9ab877"/><stop offset="1" stop-color="#5e5a3e"/></linearGradient>
      <linearGradient id="roomD" x1="0" y1="0" x2="0" y2="1"><stop offset="0" stop-color="#a57a52"/><stop offset="1" stop-color="#e5d6c0"/></linearGradient>
    </defs>
    <rect x="39" y="62" width="135" height="93" fill="url(#roomA)" role="img" aria-label="Sunroom with new white windows"/>
    <rect x="186" y="62" width="135" height="93" fill="url(#roomB)" role="img" aria-label="Bright room with tall white windows"/>
    <rect x="39" y="162" width="135" height="93" fill="url(#roomC)" role="img" aria-label="Living room with a garden view through windows"/>
    <rect x="186" y="162" width="135" height="93" fill="url(#roomD)" role="img" aria-label="Warm living room with a row of windows"/>
  </svg>

  <div class="contacts">
    <div class="contact"><svg viewBox="0 0 16 16"><rect x="1" y="3" width="14" height="10" fill="none" stroke="#fff" stroke-width="1.4"/><path d="M1 3l7 6 7-6" fill="none" stroke="#fff" stroke-width="1.4"/></svg><span>admin@rtframers-example.com</span></div>
    <div class="contact"><svg viewBox="0 0 16 16"><path d="M2 6c0-2 2-3 6-3s6 1 6 3v1h-3V5H5v2H2z" fill="#fff"/><rect x="4" y="8" width="8" height="6" rx="1" fill="#fff"/></svg><span>360-555-0148</span></div>
    <div class="contact"><svg viewBox="0 0 16 16"><rect x="5" y="1" width="7" height="14" rx="1.5" fill="none" stroke="#fff" stroke-width="1.5"/><rect x="7" y="3" width="3" height="5" fill="#fff"/></svg><span>425-555-0172</span></div>
    <div class="contact"><svg viewBox="0 0 16 16"><circle cx="8" cy="8" r="6.5" fill="none" stroke="#fff" stroke-width="1.2"/><ellipse cx="8" cy="8" rx="3" ry="6.5" fill="none" stroke="#fff" stroke-width="1.2"/><path d="M1.5 8h13" stroke="#fff" stroke-width="1.2"/></svg><span>www.rtframers-example.com</span></div>
  </div>

  <div class="address-bar">
    <svg viewBox="0 0 14 16"><path d="M7 0a6 6 0 0 0-6 6c0 4 6 10 6 10s6-6 6-10a6 6 0 0 0-6-6z" fill="#fff"/><circle cx="7" cy="6" r="2.2" fill="var(--maroon)"/></svg>
    <span>1200 Cedar Lane NE, Lakeview,<br>Washington 98000, United States</span>
  </div>
</section>

<section class="card back">
  <div class="back-panel"></div>
  <div class="back-corner"></div>
  <div class="back-brand"><div class="square"></div><span>R.T. FRAMERS</span></div>
  <div class="rebates">
    <p class="rebate">For customers who have Electric heated homes can receive $6 per square foot for each window</p>
    <p class="rebate">Patio door and for Natural gas heated homes, they can get $75.00 per window and patio door.</p>
    <p class="rebate">The $6 per square foot for electric heated customers is the better rebate averaging about $1000.00 for a house with 10 windows and a patio door.</p>
  </div>
  <p class="back-address">1200 Cedar Lane NE,<br>Lakeview, Washington<br>98000, United States</p>
  <div class="back-contacts">
    <div class="back-contact"><svg viewBox="0 0 16 16"><rect x="1" y="3" width="14" height="10" fill="none" stroke="#d8d8d8" stroke-width="1.3"/><path d="M1 3l7 6 7-6" fill="none" stroke="#d8d8d8" stroke-width="1.3"/></svg>admin@rtframers-example.com</div>
    <div class="back-contact"><svg viewBox="0 0 16 16"><path d="M2 6c0-2 2-3 6-3s6 1 6 3v1h-3V5H5v2H2z" fill="#d8d8d8"/><rect x="4" y="8" width="8" height="6" rx="1" fill="#d8d8d8"/></svg>360-555-0148</div>
    <div class="back-contact"><svg viewBox="0 0 16 16"><rect x="5" y="1" width="7" height="14" rx="1.5" fill="none" stroke="#d8d8d8" stroke-width="1.5"/><rect x="7" y="3" width="3" height="5" fill="#d8d8d8"/></svg>425-555-0172</div>
    <div class="back-contact"><svg viewBox="0 0 16 16"><circle cx="8" cy="8" r="6.5" fill="none" stroke="#d8d8d8" stroke-width="1.2"/><ellipse cx="8" cy="8" rx="3" ry="6.5" fill="none" stroke="#d8d8d8" stroke-width="1.2"/><path d="M1.5 8h13" stroke="#d8d8d8" stroke-width="1.2"/></svg>www.rtframers-example.com</div>
  </div>
</section>

</body>
</html>
```